Funeral Services Web Site

We need a website for a Funeral Services company. The choice of colors is free of charge. One Page Website with 8 sections. Menu: - Home - Our Services - Obituaries -> link to another page. - Our Shop - Funeral Monument - Funeral Contract - Contact Us

Target Market(s)

Every one need Funeral Services

Coding

Coded - Design and coding required

Number of Pages Required

2 page

Font styles to use
Sans Serif
Script

Colors

Designer to choose colors to be used in the design.

```html
<!DOCTYPE html>
<html lang="en">
<head>
<meta charset="utf-8">
<title>Maison Verlaine – Funeral Services</title>
<link rel="stylesheet" href="https://fonts.googleapis.com/css2?family=Cinzel:wght@400;700&family=Oswald:wght@500;600&family=Open+Sans:ital,wght@0,400;0,600;0,700;1,400&display=swap">
<style>
:root{
  --brown:#6b5a45;
  --brown-dark:#54463a;
  --brown-deep:#3f352c;
  --footer:#65543f;
  --ink:#3b3b3b;
  --muted:#6f6f6f;
  --page:#ffffff;
  --soft:#efefef;
  --line:#d6d6d6;
}
*{box-sizing:border-box;margin:0;padding:0}
html,body{width:1200px;height:3680px;overflow:hidden;background:var(--page)}
body{font-family:"Open Sans",Arial,sans-serif;color:var(--ink);font-size:15px;line-height:1.6}
.canvas{position:relative;width:1200px;height:3680px;overflow:hidden}
.btn{display:inline-block;background:var(--brown);color:#fff;font-size:12px;font-weight:700;letter-spacing:.5px;padding:8px 18px;text-transform:uppercase;line-height:1.4}
.section-title{font-family:"Cinzel",Georgia,serif;font-size:38px;color:var(--brown-deep);text-align:center;letter-spacing:1px;line-height:1.3}
.title-rule{width:180px;height:2px;background:var(--brown);margin:14px auto 0}

/* header */
.site-header{position:absolute;top:0;left:0;width:1200px;height:224px;background:#f6f6f6}
.tagline{position:absolute;left:84px;top:0;background:var(--brown);color:#fff;font-size:13px;padding:8px 18px}
.brand{position:absolute;left:84px;top:88px;display:flex;align-items:center;gap:14px}
.brand-mark{width:46px;height:46px;border-radius:50%;background:var(--brown)}
.brand-name{font-family:"Cinzel",Georgia,serif;font-weight:700;font-size:42px;color:var(--brown-deep);line-height:1}
.top-contacts{position:absolute;right:84px;top:12px;display:flex;gap:28px;font-size:13px;color:var(--muted)}
.top-contacts span{display:flex;align-items:center;gap:6px}
.search{position:absolute;left:500px;top:106px;width:310px;height:44px;background:#fff;border:1px solid var(--line);display:flex}
.search input{flex:1;border:0;padding:0 14px;font:14px "Open Sans",sans-serif;color:var(--muted);background:transparent}
.search-btn{width:80px;background:var(--brown);display:flex;align-items:center;justify-content:center}
.header-icons{position:absolute;left:900px;top:110px;display:flex;gap:18px}
.main-nav{position:absolute;top:224px;left:0;width:1200px;height:48px;background:var(--brown)}
.main-nav ul{list-style:none;display:flex;justify-content:space-between;padding:0 84px}
.main-nav li{color:#fff;font-size:14px;font-weight:600;line-height:48px;padding:0 28px}
.main-nav li.active{background:var(--brown-deep)}

/* hero */
.hero{position:absolute;top:272px;left:0;width:1200px;height:468px;background:linear-gradient(90deg,#d9d9d9,#ececec 60%,#f2f2f2)}
.hero-photo{position:absolute;left:0;top:0;width:470px;height:468px;background:radial-gradient(circle at 40% 35%,#d98a8a,#9a6a52 45%,#5a4636 80%)}
.hero-text{position:absolute;left:760px;top:110px;width:380px}
.hero-text h1{font-family:"Oswald",Arial,sans-serif;font-weight:600;font-size:40px;line-height:1.1;color:var(--brown-deep);text-align:right}
.hero-text p{font-size:13px;color:var(--muted);text-align:right;margin:16px 0 26px}
.hero-arrow{position:absolute;right:16px;top:252px;width:40px;height:40px;border-radius:50%;background:var(--brown-deep);display:flex;align-items:center;justify-content:center}

/* welcome */
.welcome{position:absolute;top:740px;left:0;width:1200px;height:400px;background:#fff}
.welcome-text{position:absolute;left:84px;top:70px;width:560px}
.welcome-text h2{font-family:"Cinzel",Georgia,serif;font-size:36px;color:var(--brown-deep);letter-spacing:1px}
.welcome-text p{font-size:14px;color:var(--muted);margin:14px 0}
.welcome-photo{position:absolute;left:690px;top:62px;width:420px;height:290px;background:linear-gradient(135deg,#3d3026,#7b5c3f 55%,#2c241d)}

/* services */
.services{position:absolute;top:1140px;left:0;width:1200px;height:460px;background:var(--soft)}
.services .section-title{margin-top:66px}
.service-grid{display:flex;justify-content:space-between;padding:0 150px;margin-top:48px}
.service{width:200px;text-align:center;border-right:1px solid var(--line);padding-right:16px}
.service:last-child{border-right:0}
.service h3{font-family:"Cinzel",Georgia,serif;font-size:18px;color:var(--brown-deep);margin:12px 0 6px}
.service p{font-size:12px;color:var(--muted);line-height:1.5;margin-bottom:10px}
.service .btn{font-size:10px;padding:4px 10px}

/* obituaries */
.obituaries{position:absolute;top:1600px;left:0;width:1200px;height:560px;background:#e6e6e6}
.obituaries .section-title{margin-top:60px}
.obit-grid{display:flex;justify-content:center;gap:30px;margin-top:46px}
.obit{width:225px}
.obit-portrait{position:relative;height:230px;background:var(--brown)}
.obit-photo{position:absolute;left:45px;top:30px;width:135px;height:160px;background:linear-gradient(#4a3b30,#2e2620)}
.obit-name{position:absolute;left:0;bottom:0;width:100%;text-align:center;color:#fff;font-size:22px;padding:4px 0;background:rgba(40,32,26,.55)}
.obit-meta{font-size:12px;color:var(--muted);padding:10px 28px;line-height:1.5}
.dots{display:flex;justify-content:center;gap:10px;margin-top:26px}
.dots i{width:11px;height:11px;border-radius:50%;background:#aaa}
.dots i:first-child{background:var(--brown-deep)}

/* quote */
.quote{position:absolute;top:2160px;left:0;width:1200px;height:460px;background:linear-gradient(90deg,#4a3a1c 0%,#2a2520 45%,#1c2430 100%)}
.quote blockquote{position:absolute;left:180px;top:180px;width:860px;color:#fff;font-size:24px;line-height:1.5}
.quote cite{position:absolute;right:140px;top:300px;color:#fff;font-style:normal;font-size:14px}

/* blog */
.blog{position:absolute;top:2620px;left:0;width:1200px;height:580px;background:#fff}
.blog .section-title{margin-top:34px}
.blog-grid{display:flex;justify-content:center;gap:80px;margin-top:30px}
.post{width:380px;text-align:center}
.post-photo{height:250px}
.post h3{font-family:"Cinzel",Georgia,serif;font-size:24px;line-height:1.3;color:var(--brown-deep);margin-top:16px}
.post time{display:block;font-size:12px;color:var(--muted);font-style:italic}
.post p{font-size:13px;color:var(--muted);margin-top:8px;line-height:1.55}
.post .btn{font-size:10px;padding:2px 10px;margin-left:6px}

/* footer */
.site-footer{position:absolute;top:3200px;left:0;width:1200px;height:480px;background:var(--footer);color:#f1ebe3}
.footer-cols{display:flex;padding:70px 84px 0;gap:60px}
.footer-col h4{font-size:17px;font-weight:700;letter-spacing:.5px;margin-bottom:16px;color:#fff}
.footer-col p,.footer-col li{font-size:13px;line-height:1.7}
.footer-about{width:420px}
.footer-about .btn{background:var(--brown-deep);margin-top:10px;font-size:10px;padding:4px 12px}
.footer-contact{width:280px}
.social{display:flex;gap:10px;margin-top:16px}
.social i{width:30px;height:30px;border:1px solid #f1ebe3}
.footer-links ul{list-style:none}
.footer-bottom{position:absolute;bottom:0;left:0;width:1200px;height:54px;background:var(--brown-dark);display:flex;justify-content:space-between;align-items:center;padding:0 84px;font-size:12px}
</style>
</head>
<body>
<div class="canvas">

<header class="site-header">
  <div class="tagline">A Funeral Services company</div>
  <div class="brand"><span class="brand-mark"></span><span class="brand-name">Maison<br>Verlaine</span></div>
  <div class="top-contacts">
    <span><svg width="14" height="14" viewBox="0 0 24 24"><path d="M6 2l4 4-2 3c1 3 4 6 7 7l3-2 4 4-3 4C10 21 3 14 2 5z" fill="#6b5a45"/></svg>555 0142 880</span>
    <span><svg width="12" height="14" viewBox="0 0 20 24"><path d="M10 0a8 8 0 018 8c0 6-8 16-8 16S2 14 2 8a8 8 0 018-8z" fill="#6b5a45"/><circle cx="10" cy="8" r="3" fill="#fff"/></svg>48 Linden Avenue, Ashford Hill</span>
    <span><svg width="14" height="14" viewBox="0 0 24 24"><circle cx="12" cy="8" r="5" fill="#6b5a45"/><path d="M2 24c0-7 20-7 20 0z" fill="#6b5a45"/></svg>Login</span>
  </div>
  <div class="search"><input value="Search" aria-label="Search"><span class="search-btn"><svg width="20" height="20" viewBox="0 0 24 24"><circle cx="10" cy="10" r="7" stroke="#fff" stroke-width="2.5" fill="none"/><path d="M15 15l7 7" stroke="#fff" stroke-width="2.5"/></svg></span></div>
  <div class="header-icons">
    <svg width="36" height="32" viewBox="0 0 36 32"><path d="M2 3h6l4 18h18l4-13H10" stroke="#6b5a45" stroke-width="3" fill="none"/><circle cx="14" cy="27" r="3" fill="#6b5a45"/><circle cx="27" cy="27" r="3" fill="#6b5a45"/></svg>
    <svg width="32" height="30" viewBox="0 0 32 30"><path d="M16 28S2 19 2 10a7 7 0 0114-2 7 7 0 0114 2c0 9-14 18-14 18z" fill="#6b5a45"/></svg>
  </div>
</header>

<nav class="main-nav"><ul>
  <li class="active">Home</li><li>Our Services</li><li>Obituaries</li><li>Our Shop ▾</li><li>Funeral Monument</li><li>Funeral Contract</li><li>Contact Us</li>
</ul></nav>

<section class="hero">
  <div class="hero-photo" role="img" aria-label="Basket of pink and white flowers"></div>
  <div class="hero-text">
    <h1>GREET YOUR LOVED<br>ONES WITH LOVE</h1>
    <p>Lorem ipsum dolor sit amet, consectetur adipiscing elit, sed do eiusmod tempor incididunt ut labore et dolore magna aliqua.</p>
    <span class="btn">Read More</span>
  </div>
  <span class="hero-arrow"><svg width="14" height="14" viewBox="0 0 14 14"><path d="M4 1l6 6-6 6" stroke="#fff" stroke-width="2.5" fill="none"/></svg></span>
</section>

<section class="welcome">
  <div class="welcome-text">
    <h2>WELCOME</h2>
    <p>Lorem ipsum is simply dummy text of the printing and typesetting industry. Lorem ipsum has been the industry's standard dummy text ever since the 1500s, when an unknown printer took a galley of type and scrambled it to make a type specimen book.</p>
    <p>Desktop publishing software like Aldus PageMaker including versions of Lorem Ipsum. Lorem ipsum is simply dummy text of the printing and typesetting industry, standard dummy text ever since the 1500s.</p>
    <span class="btn">More Info</span>
  </div>
  <div class="welcome-photo" role="img" aria-label="Wooden rosary resting on an old book"></div>
</section>

<section class="services">
  <h2 class="section-title">OUR SERVICES</h2>
  <div class="title-rule"></div>
  <div class="service-grid">
    <div class="service">
      <svg width="60" height="56" viewBox="0 0 60 56" fill="none" stroke="#3f352c" stroke-width="2"><path d="M6 54h48M10 54V24h40v30M4 24l26-18 26 18M18 54V34h8v20M34 54V34h8v20"/></svg>
      <h3>Burial</h3><p>Lorem ipsum is simply dummy text of the printing and typesetting industry.</p><span class="btn">Read More</span>
    </div>
    <div class="service">
      <svg width="60" height="56" viewBox="0 0 60 56" fill="none" stroke="#3f352c" stroke-width="2"><path d="M22 4h16v6H22zM20 10h20c4 8 6 14 6 22 0 12-7 20-16 20S14 44 14 32c0-8 2-14 6-22z"/></svg>
      <h3>Cremation</h3><p>Lorem ipsum is simply dummy text of the printing and typesetting industry.</p><span class="btn">Read More</span>
    </div>
    <div class="service">
      <svg width="60" height="56" viewBox="0 0 60 56" fill="none" stroke="#3f352c" stroke-width="2"><path d="M22 2h16l6 14-4 38H20l-4-38z"/><path d="M30 14v18M24 20h12"/></svg>
      <h3>Caskets</h3><p>Lorem ipsum is simply dummy text of the printing and typesetting industry.</p><span class="btn">Read More</span>
    </div>
    <div class="service">
      <svg width="60" height="56" viewBox="0 0 60 56" fill="none" stroke="#3f352c" stroke-width="2"><circle cx="30" cy="14" r="8"/><circle cx="18" cy="22" r="6"/><circle cx="42" cy="22" r="6"/><path d="M30 22v32M18 28l12 14M42 28L30 42M22 54h16"/></svg>
      <h3>Send Flowers</h3><p>Lorem ipsum is simply dummy text of the printing and typesetting industry.</p><span class="btn">Read More</span>
    </div>
  </div>
</section>

<section class="obituaries">
  <h2 class="section-title">OBITUARIES</h2>
  <div class="title-rule"></div>
  <div class="obit-grid">
    <article class="obit"><div class="obit-portrait"><div class="obit-photo" role="img" aria-label="Portrait of the deceased"></div><div class="obit-name">Henri Lamotte</div></div><p class="obit-meta">Death : 12/10/2019<br>Location : New York</p></article>
    <article class="obit"><div class="obit-portrait"><div class="obit-photo" role="img" aria-label="Portrait of the deceased"></div><div class="obit-name">Adam Joly</div></div><p class="obit-meta">Death : 12/10/2019<br>Location : Washington</p></article>
    <article class="obit"><div class="obit-portrait"><div class="obit-photo" role="img" aria-label="Portrait of the deceased"></div><div class="obit-name">Richard Poe</div></div><p class="obit-meta">Death : 12/10/2019<br>Location : New Jersey</p></article>
    <article class="obit"><div class="obit-portrait"><div class="obit-photo" role="img" aria-label="Portrait of the deceased"></div><div class="obit-name">Max Durand</div></div><p class="obit-meta">Death : 12/10/2019<br>Location : California</p></article>
  </div>
  <div class="dots"><i></i><i></i><i></i><i></i></div>
</section>

<section class="quote" role="img" aria-label="Yellow flowers against a dark sky">
  <blockquote>“ For if we live, we live to the Lord, and if we die, we die to the Lord. So then, whether we live or whether we die, we are the Lord's. ”</blockquote>
  <cite>- Bible</cite>
</section>

<section class="blog">
  <h2 class="section-title">OUR BLOG</h2>
  <div class="title-rule"></div>
  <div class="blog-grid">
    <article class="post">
      <div class="post-photo" role="img" aria-label="Hands resting on an open Bible" style="background:linear-gradient(135deg,#7a3b2a,#b0604a 50%,#3a211a)"></div>
      <h3>Prayer Reaching God</h3><time>March 28, 2019</time>
      <p>Lorem ipsum is simply dummy text of the printing and typesetting industry. Lorem ipsum has been the standard dummy text ever <span class="btn">Read More</span></p>
    </article>
    <article class="post">
      <div class="post-photo" role="img" aria-label="Gravestone in a dim cemetery at dusk" style="background:linear-gradient(160deg,#1b1a17,#4a3a24 60%,#8a6a3a)"></div>
      <h3>Resting Soul</h3><time>March 28, 2019</time>
      <p>Lorem ipsum is simply dummy text of the printing and typesetting industry. Lorem ipsum has been the standard dummy text ever <span class="btn">Read More</span></p>
    </article>
  </div>
</section>

<footer class="site-footer">
  <div class="footer-cols">
    <div class="footer-col footer-about">
      <h4>MAISON VERLAINE</h4>
      <p>Lorem ipsum is simply dummy text of the printing and typesetting industry. Lorem ipsum has been the industry's standard dummy text ever since the 1500s, when an unknown printer took a galley of type and scrambled it to make a type specimen book.</p>
      <span class="btn">More Info</span>
    </div>
    <div class="footer-col footer-contact">
      <h4>CONTACT &amp; CONNECTS</h4>
      <p>48 Linden Avenue, Ashford Hill</p>
      <p>Phone : 555 0142 880</p>
      <p>Mail : info@verlaine.example</p>
      <div class="social"><i></i><i></i><i></i></div>
    </div>
    <div class="footer-col footer-links">
      <h4>QUICK LINKS</h4>
      <ul><li>Our Services</li><li>Obituaries</li><li>Our Shop</li><li>Funeral Monument</li><li>Funeral Contract</li><li>Contact Us</li></ul>
    </div>
  </div>
  <div class="footer-bottom"><span>All Copyrights © 2019 Maison Verlaine. All rights reserved.</span><span>Terms &amp; Conditions | Privacy Policy</span></div>
</footer>

</div>
</body>
</html>
```